I need cover art for my first album

I am releasing my first album and I need cover art for the CD  packaging. The art would also be used in Tunevale and other streaming services. The music is dark, experimental electronic music. It includes lots of soundscapes with industrial, metallic sounds. Similar artists include Grevhald and Ivor Pennick. The album's concept is inspired by the loneliness and inherent dangers of long-term space travel and living alone in cold, distant space stations.
You can hear a rough cut of one of the tracks for the album at https://echoloft.net/kelvorant/tidegrove.

Colors
Designer to choose colors to be used in the design.
Requirements
Must have
- The design should be abstract and minimalist but not only grayscale. I would like to see color used in ways that convey feelings. Provide a sense of movement.
Should not have
- No images of moons or planets. Please don't be literal with the "space" theme.

```html
<!DOCTYPE html>
<html lang="en">
<head>
<meta charset="utf-8">
<title>Silence After The Hull — Album Cover</title>
<link href="https://fonts.googleapis.com/css2?family=Raleway:wght@400&display=swap" rel="stylesheet">
<style>
  :root {
    --deep-navy: #1d3558;
    --mid-navy: #142843;
    --shadow-navy: #0d1a2e;
    --night: #05080e;
    --drift-haze: rgba(120, 150, 190, 0.10);
    --title-ink: #e2e4e8;
  }
  html, body {
    margin: 0;
    padding: 0;
    width: 1200px;
    height: 1200px;
    overflow: hidden;
    background: var(--night);
  }
  .cover {
    position: relative;
    width: 1200px;
    height: 1200px;
    overflow: hidden;
    background: var(--night);
  }
  .debris-field {
    position: absolute;
    inset: 0;
    background:
      linear-gradient(118deg, transparent 0%, transparent 18%, var(--drift-haze) 24%, transparent 31%, transparent 46%, var(--drift-haze) 52%, transparent 58%, transparent 100%),
      linear-gradient(124deg, transparent 0%, transparent 62%, rgba(120, 150, 190, 0.06) 68%, transparent 74%),
      radial-gradient(ellipse 70% 40% at 12% 100%, rgba(0, 0, 0, 0.55) 0%, transparent 70%),
      radial-gradient(ellipse 95% 75% at 45% 18%, var(--deep-navy) 0%, var(--mid-navy) 48%, transparent 82%),
      linear-gradient(180deg, #19304f 0%, #15294a 40%, #112039 62%, var(--shadow-navy) 80%, var(--night) 100%);
  }
  .album-title {
    position: absolute;
    left: 0;
    right: 0;
    top: 567px;
    margin: 0;
    padding-left: 28px;
    text-align: center;
    font-family: "Raleway", "Helvetica Neue", Arial, sans-serif;
    font-weight: 400;
    font-size: 42px;
    letter-spacing: 0.15em;
    line-height: 1;
    color: var(--title-ink);
    white-space: nowrap;
  }
</style>
</head>
<body>
  <main class="cover">
    <div class="debris-field" role="img" aria-label="Fragments of station wreckage and solar panels tumbling diagonally through deep blue darkness, fading to black at the bottom"></div>
    <h1 class="album-title">SILENCE AFTER THE HULL</h1>
  </main>
</body>
</html>
```